Business Cards for a law firm

Business cards for our law firm. Use our silhoette logo and OAK HARBOR - check our website (www.oakharbor-legal.com)

Contact Information for Business Card

our silhouette logo, OAK HARBOR, 800-555-0147, Dorian Kestrup, dorian@oakharbor-legal.com

Requirements
Must have
• our silhouette logo, OAK HARBOR, 800-555-0147, Dorian Kestrup, dorian@oakharbor-legal.com

```html
<!DOCTYPE html>
<html lang="en">
<head>
<meta charset="utf-8">
<title>Oak Harbor – Business Cards</title>
<link rel="stylesheet" href="https://fonts.googleapis.com/css2?family=Montserrat:wght@300;400;500;700&display=swap">
<style>
  :root {
    --backdrop: #8a8a88;
    --navy: #23346b;
    --navy-deep: #141d45;
    --navy-light: #6a80c4;
    --paper: #ffffff;
    --ink-grey: #6b6b72;
    --rule: #3a4a80;
  }
  * { box-sizing: border-box; margin: 0; padding: 0; }
  html, body {
    width: 1200px; height: 791px; overflow: hidden;
    background: var(--backdrop);
    font-family: "Montserrat", sans-serif;
  }
  .stage {
    position: relative; width: 1200px; height: 791px;
  }
  .card {
    position: absolute; top: 246px;
    width: 520px; height: 298px;
    box-shadow: 0 6px 18px rgba(0,0,0,0.25);
    overflow: hidden;
  }
  /* Contact side */
  .card-contact {
    left: 60px; background: var(--paper);
    border-bottom: 3px solid var(--navy);
  }
  .brand-block {
    position: absolute; left: 34px; top: 134px;
    display: flex; align-items: center; gap: 10px;
  }
  .brand-mark {
    width: 14px; height: 14px; background: var(--navy);
  }
  .brand-name {
    color: var(--navy); font-weight: 500;
    font-size: 20px; letter-spacing: 2.5px;
  }
  .divider {
    position: absolute; left: 236px; top: 98px;
    width: 1.5px; height: 102px; background: var(--rule);
  }
  .person-block {
    position: absolute; left: 262px; top: 96px;
  }
  .person-name {
    color: var(--navy); font-weight: 700;
    font-size: 19px; letter-spacing: 0.3px;
    margin-bottom: 12px;
  }
  .contact-list { list-style: none; }
  .contact-item {
    display: flex; align-items: center; gap: 9px;
    color: var(--ink-grey); font-weight: 400;
    font-size: 13px; line-height: 23px;
  }
  .contact-icon { width: 11px; height: 11px; flex: none; }

  /* Brand side */
  .card-brand {
    left: 620px; background: var(--navy);
  }
  .hero-art {
    position: absolute; left: 28px; top: 60px;
    width: 230px; height: 238px;
    background: linear-gradient(160deg, var(--navy-deep) 0%, #2b3d80 55%, var(--navy-light) 100%);
    opacity: 0.9;
    border-radius: 60px 60px 0 0;
  }
  .brand-title {
    position: absolute; right: 30px; bottom: 44px;
    color: var(--paper); font-weight: 500;
    font-size: 26px; letter-spacing: 3px;
  }
</style>
</head>
<body>
<main class="stage">
  <section class="card card-contact">
    <div class="brand-block">
      <span class="brand-mark"></span>
      <span class="brand-name">OAK HARBOR</span>
    </div>
    <div class="divider"></div>
    <div class="person-block">
      <p class="person-name">DORIAN KESTRUP</p>
      <ul class="contact-list">
        <li class="contact-item">
          <svg class="contact-icon" viewBox="0 0 12 12"><path d="M2.5 1 L4.5 1 L5.3 3.5 L4 4.5 Q5 7 7.5 8 L8.5 6.7 L11 7.5 L11 9.5 Q10.5 11 9 11 Q2 10 1 3 Q1 1.5 2.5 1Z" fill="var(--navy)"/></svg>
          <span>800-555-0147</span>
        </li>
        <li class="contact-item">
          <svg class="contact-icon" viewBox="0 0 12 12"><rect x="0.5" y="2" width="11" height="8" fill="var(--navy)"/><path d="M0.5 2 L6 6.5 L11.5 2" fill="none" stroke="#fff" stroke-width="1"/></svg>
          <span>dorian@oakharbor-legal.com</span>
        </li>
        <li class="contact-item">
          <svg class="contact-icon" viewBox="0 0 12 12"><circle cx="6" cy="6" r="5.5" fill="var(--navy)"/><path d="M0.5 6 H11.5 M6 0.5 Q3 6 6 11.5 M6 0.5 Q9 6 6 11.5" fill="none" stroke="#fff" stroke-width="0.8"/></svg>
          <span>www.oakharbor-legal.com</span>
        </li>
      </ul>
    </div>
  </section>

  <section class="card card-brand">
    <div class="hero-art" role="img" aria-label="Silhouettes of two standing men in blue tones"></div>
    <p class="brand-title">OAK HARBOR</p>
  </section>
</main>
</body>
</html>
```